Personal Business Card design contest for freelance work

Include

Proflink.example/in/DanielMWhitacre (as URL and/or QR Code)
Daniel Whitacre
(555) 014-2938
DanielMWhitacre@Mailnest.example
Lakemont, NV

Industry/Entity Type

Business

```html
<!DOCTYPE html>
<html lang="en">
<head>
<meta charset="utf-8">
<title>Daniel Whitacre – Business Card</title>
<link rel="stylesheet" href="https://fonts.googleapis.com/css2?family=Crimson+Pro:wght@500&family=Lato:wght@400&display=swap">
<style>
  :root {
    --backdrop: #1c1c1c;
    --card-light: #f4f4f4;
    --card-shade: #d9d9d9;
    --ink-black: #050505;
    --accent-blue: #1e9ad6;
    --contact-white: #f2f2f2;
    --portrait-top: #9a7a62;
    --portrait-bottom: #2b2d33;
  }
  html, body {
    margin: 0;
    width: 1200px;
    height: 873px;
    overflow: hidden;
    background: var(--backdrop);
  }
  .card {
    position: absolute;
    left: 180px;
    top: 196px;
    width: 840px;
    height: 480px;
    border-radius: 28px;
    overflow: hidden;
    background: linear-gradient(160deg, var(--card-light) 0%, var(--card-light) 45%, var(--card-shade) 100%);
    box-shadow: 0 18px 40px rgba(0,0,0,0.55);
  }
  .card-art {
    position: absolute;
    inset: 0;
    width: 840px;
    height: 480px;
  }
  .greeting {
    position: absolute;
    left: 40px;
    top: 72px;
    width: 420px;
    margin: 0;
    text-align: center;
    font-family: "Crimson Pro", Georgia, serif;
    font-weight: 500;
    font-size: 46px;
    line-height: 1.2;
    color: var(--accent-blue);
  }
  .contact-list {
    position: absolute;
    left: 36px;
    top: 338px;
    margin: 0;
    padding: 0;
    list-style: none;
    font-family: "Lato", Arial, sans-serif;
    font-size: 17px;
    color: var(--contact-white);
  }
  .contact-list li {
    display: flex;
    align-items: center;
    height: 31px;
  }
  .contact-icon {
    width: 18px;
    height: 18px;
    margin-right: 16px;
    flex: none;
  }
</style>
</head>
<body>
  <div class="card">
    <svg class="card-art" viewBox="0 0 840 480">
      <defs>
        <linearGradient id="portraitTone" x1="0" y1="0" x2="0" y2="1">
          <stop offset="0" stop-color="var(--portrait-top)"/>
          <stop offset="0.45" stop-color="#c9a68a"/>
          <stop offset="1" stop-color="var(--portrait-bottom)"/>
        </linearGradient>
      </defs>
      <rect class="portrait" x="572" y="24" width="196" height="262" rx="18" fill="url(#portraitTone)" role="img" aria-label="Illustrated caricature of Daniel Whitacre in a dark suit holding a tablet"/>
      <path class="accent-wave" fill="var(--accent-blue)"
        d="M0 318 C200 232,420 276,560 288 C680 298,780 262,840 234 L840 242 C780 272,680 310,560 302 C420 292,200 252,0 340Z"/>
      <path class="dark-band" fill="var(--ink-black)"
        d="M0 340 C200 252,420 292,560 302 C680 310,780 272,840 242 L840 480 L0 480Z"/>
    </svg>

    <h1 class="greeting">Hi! I’m<br>Daniel Whitacre</h1>

    <ul class="contact-list">
      <li>
        <svg class="contact-icon" viewBox="0 0 18 18"><rect x="4" y="1" width="10" height="16" rx="2" fill="none" stroke="var(--accent-blue)" stroke-width="2"/></svg>
        (555) 014-2938
      </li>
      <li>
        <svg class="contact-icon" viewBox="0 0 18 18"><rect x="1" y="4" width="16" height="11" fill="var(--accent-blue)"/><path d="M1 4 L9 10 L17 4" fill="none" stroke="var(--ink-black)" stroke-width="1.5"/></svg>
        DanielMWhitacre@Mailnest.example
      </li>
      <li>
        <svg class="contact-icon" viewBox="0 0 18 18"><rect x="2" y="2" width="14" height="14" rx="2" fill="var(--accent-blue)"/></svg>
        Proflink.example/in/DanielMWhitacre
      </li>
      <li>
        <svg class="contact-icon" viewBox="0 0 18 18"><path d="M9 17 C4 11,3 9,3 7 A6 6 0 0 1 15 7 C15 9,14 11,9 17Z" fill="var(--accent-blue)"/><circle cx="9" cy="7" r="2.2" fill="var(--ink-black)"/></svg>
        Lakemont, NV
      </li>
    </ul>
  </div>
</body>
</html>
```